Meadow Hollow Beauty brand redesign of product labels

national rebrand of skincare product labels - same design but 6 sizes. Will be used for facial serums, body oils, bath salts, room sprays, etc. All labels to be same design - just adjusted for the different sizes. See brand document and sample label.

Bottle Specifications are located in the branding file.
Fonts included in product branding document.
Colours included in branding document.

Featuring company name and logo, product name, product feature, ingredients, size, directions, tag line. See attached sample label as example for design.

Black label base - matt.

Target Market(s)

Natural beauty, 20-60

Industry/Entity Type

farming, natural beauty

Font styles to use
Sans Serif

Requirements
Must have
• Modern, clean, homey
Nice to have
• modern clean design - using the branding colours provided
Should not have
• busy, crowded,

```html
<!DOCTYPE html>
<html lang="en">
<head>
<meta charset="utf-8">
<title>Meadow Hollow Beauty – Brighten label</title>
<link rel="stylesheet" href="https://fonts.googleapis.com/css2?family=Cabin:wght@400;600;700&family=Open+Sans:wght@400&family=Great+Vibes&display=swap">
<style>
  :root {
    --page: #e6e6e6;
    --label: #231918;
    --leaf-light: #c8e3a9;
    --leaf-teal: #6fa9a2;
    --ink-soft: #ece9e2;
    --white: #ffffff;
  }
  * { margin: 0; padding: 0; box-sizing: border-box; }
  html, body { width: 1200px; height: 1117px; overflow: hidden; background: var(--page); }
  .label {
    position: absolute; left: 210px; top: 38px;
    width: 779px; height: 1040px;
    background: var(--label);
    overflow: hidden;
    font-family: "Cabin", sans-serif;
  }
  .brand {
    position: absolute; left: 0; right: 0; top: 185px;
    text-align: center; padding-left: 26px;
    color: var(--leaf-light);
    font-family: "Cabin", sans-serif; font-weight: 400;
  }
  .brand-name { font-size: 38px; letter-spacing: 9px; line-height: 1.15; }
  .brand-mark {
    display: inline-block; width: 12px; height: 12px; border-radius: 50%;
    background: var(--leaf-teal); margin-top: 14px;
  }
  .tagline {
    position: absolute; left: 0; right: 0; top: 410px;
    text-align: center; color: var(--ink-soft);
    font-family: "Open Sans", sans-serif; font-size: 13px; letter-spacing: 0.2px;
  }
  .tagline em {
    font-family: "Great Vibes", cursive; font-style: normal;
    color: var(--leaf-light); font-size: 26px; vertical-align: -4px; margin: 0 3px;
  }
  .product-name {
    position: absolute; left: 0; right: 0; top: 486px;
    text-align: center; color: var(--leaf-light);
    font-weight: 700; font-size: 80px; letter-spacing: -2.5px; line-height: 1;
  }
  .product-claim {
    position: absolute; left: 0; right: 0; top: 583px;
    text-align: center; color: var(--leaf-light);
    font-weight: 700; font-size: 37px; line-height: 42px; letter-spacing: -0.5px;
  }
  .feature {
    position: absolute; left: 218px; width: 344px; top: 697px; height: 39px;
  }
  .feature-rule {
    position: absolute; left: 0; right: 0; top: 18px; height: 2px; background: var(--leaf-teal);
  }
  .feature-pill {
    position: absolute; left: 44px; right: 26px; top: 0; height: 39px;
    border-radius: 20px; background: var(--leaf-teal);
    color: var(--white); font-weight: 600; font-size: 22px;
    display: flex; align-items: center; justify-content: center;
  }
  .volume {
    position: absolute; left: 220px; top: 856px;
    color: var(--leaf-light); font-weight: 600; font-size: 44px; letter-spacing: -1px;
  }
  .branch-art {
    position: absolute; left: 318px; top: 737px; width: 461px; height: 303px;
    background: radial-gradient(ellipse at 60% 65%, rgba(111,169,162,0.55) 0%, rgba(200,227,169,0.25) 45%, rgba(35,25,24,0) 75%);
  }
</style>
</head>
<body>
  <main class="label">
    <div class="brand">
      <div class="brand-name">MEADOW HOLLOW<br>BEAUTY</div>
      <span class="brand-mark"></span>
    </div>
    <p class="tagline">CULTIVATING<em>beauty</em>FROM THE GROUND UP</p>
    <h1 class="product-name">BRIGHTEN</h1>
    <p class="product-claim">ROOTED IN NATURE,<br>CRAFTED WITH CARE</p>
    <div class="feature">
      <div class="feature-rule"></div>
      <div class="feature-pill">Nurturing &amp; Natural</div>
    </div>
    <p class="volume">100 ml</p>
    <div class="branch-art" role="img" aria-label="Leafy branch illustration in teal and light green"></div>
  </main>
</body>
</html>
```